varnuko.com car care product labeling with cut outs will be printed on holographic sheet.

Need to make label for eco-friendly car care products. no hazard signs.
clean and simple design minimalism
wheel cleaner
tire shiner
glass cleaner
all purpose cleaner
247x90mm
166x150mm

Target Market(s)

eco friendly car care products. europe , uae

Industry/Entity Type

car care products, eco-friendly product line

Requirements
Must have
• BW design print on holographic sheet/label .eco-friendly signs
Nice to have
• premium product look and simplicity will be at first place, can be with cut outs

```html
<!DOCTYPE html>
<html lang="en">
<head>
<meta charset="utf-8">
<title>varnuko.com — eco-friendly car care labels</title>
<link href="https://fonts.googleapis.com/css2?family=Manrope:wght@400;500;800&display=swap" rel="stylesheet">
<style>
  :root {
    --bg: #e9e9eb;
    --ink: #111111;
    --holo-pink: #f2d2ea;
    --holo-mint: #d3f3dc;
    --holo-lilac: #dad5f4;
    --holo-lemon: #f1f2cf;
    --holo-sky: #cfe2f6;
    --holo-pearl: #ecebf0;
  }
  * { margin: 0; padding: 0; box-sizing: border-box; }
  html, body { width: 1200px; height: 1200px; overflow: hidden; }
  body {
    background: var(--bg);
    font-family: "Manrope", sans-serif;
    color: var(--ink);
    position: relative;
  }
  .label {
    position: absolute;
    width: 260px;
    height: 760px;
    border-radius: 6px;
    overflow: hidden;
    background:
      linear-gradient(160deg, transparent 0%, var(--holo-pink) 18%, transparent 32%, var(--holo-sky) 46%, transparent 58%, var(--holo-pink) 72%, transparent 86%),
      linear-gradient(35deg, var(--holo-lemon) 0%, var(--holo-mint) 25%, var(--holo-lilac) 45%, var(--holo-mint) 65%, var(--holo-lemon) 82%, var(--holo-lilac) 100%),
      var(--holo-pearl);
    background-blend-mode: multiply, normal, normal;
    box-shadow: 0 10px 30px rgba(0,0,0,0.08);
  }
  .label--glass { left: 130px; top: 300px; }
  .label--wheel { left: 470px; top: 150px; }
  .label--all { left: 810px; top: 330px; }

  .label__brand {
    position: absolute;
    left: 50%;
    top: 40px;
    height: 470px;
    transform: translateX(-50%) rotate(180deg);
    writing-mode: vertical-rl;
    font-weight: 800;
    font-size: 112px;
    line-height: 1;
    letter-spacing: -2px;
    text-align: center;
  }
  .label__info {
    position: absolute;
    left: 0; right: 0;
    top: 545px;
    text-align: center;
  }
  .label__product {
    display: inline-block;
    font-weight: 500;
    font-size: 25px;
    padding: 0 8px 6px;
    border-bottom: 1.5px solid var(--ink);
  }
  .label--all .label__product { font-size: 22px; }
  .label__claim {
    margin-top: 10px;
    font-size: 16px;
    font-weight: 400;
  }
  .label__marks {
    position: absolute;
    left: 0; right: 0;
    top: 670px;
    display: flex;
    justify-content: center;
    gap: 26px;
  }
  .label__marks svg { width: 50px; height: 50px; }
</style>
</head>
<body>

  <article class="label label--glass">
    <div class="label__brand">varnuko</div>
    <div class="label__info">
      <div class="label__product">glass cleaner</div>
      <p class="label__claim">100% eco-friendly</p>
    </div>
    <div class="label__marks">
      <svg viewBox="0 0 50 50" role="img" aria-label="Eco certification badge"><circle cx="25" cy="25" r="21" fill="none" stroke="#111" stroke-width="2"/><circle cx="25" cy="25" r="12" fill="#111"/></svg>
      <svg viewBox="0 0 50 50" role="img" aria-label="Recyclable"><g fill="none" stroke="#111" stroke-width="5" stroke-linejoin="round"><path d="M18 14 L25 6 L32 17"/><path d="M40 28 L44 38 L30 40"/><path d="M20 40 L8 38 L13 27"/></g><path d="M29 12 l6 7 l-9 1 z M34 39 l-6 -5 l-1 9 z M10 30 l9 -2 l-3 -8 z" fill="#111"/></svg>
    </div>
  </article>

  <article class="label label--wheel">
    <div class="label__brand">varnuko</div>
    <div class="label__info">
      <div class="label__product">wheel cleaner</div>
      <p class="label__claim">100% eco-friendly</p>
    </div>
    <div class="label__marks">
      <svg viewBox="0 0 50 50" role="img" aria-label="Eco certification badge"><circle cx="25" cy="25" r="21" fill="none" stroke="#111" stroke-width="2"/><circle cx="25" cy="25" r="12" fill="#111"/></svg>
      <svg viewBox="0 0 50 50" role="img" aria-label="Recyclable"><g fill="none" stroke="#111" stroke-width="5" stroke-linejoin="round"><path d="M18 14 L25 6 L32 17"/><path d="M40 28 L44 38 L30 40"/><path d="M20 40 L8 38 L13 27"/></g><path d="M29 12 l6 7 l-9 1 z M34 39 l-6 -5 l-1 9 z M10 30 l9 -2 l-3 -8 z" fill="#111"/></svg>
    </div>
  </article>

  <article class="label label--all">
    <div class="label__brand">varnuko</div>
    <div class="label__info">
      <div class="label__product">all purpose cleaner</div>
      <p class="label__claim">100% eco-friendly</p>
    </div>
    <div class="label__marks">
      <svg viewBox="0 0 50 50" role="img" aria-label="Eco certification badge"><circle cx="25" cy="25" r="21" fill="none" stroke="#111" stroke-width="2"/><circle cx="25" cy="25" r="12" fill="#111"/></svg>
      <svg viewBox="0 0 50 50" role="img" aria-label="Recyclable"><g fill="none" stroke="#111" stroke-width="5" stroke-linejoin="round"><path d="M18 14 L25 6 L32 17"/><path d="M40 28 L44 38 L30 40"/><path d="M20 40 L8 38 L13 27"/></g><path d="M29 12 l6 7 l-9 1 z M34 39 l-6 -5 l-1 9 z M10 30 l9 -2 l-3 -8 z" fill="#111"/></svg>
    </div>
  </article>

</body>
</html>
```